Cleaning service website design

We need a new nice web design(logo will be the same) for a new cleaning service Company:

Informations about Company and logo you can take from flyers in attachments.

This is a cleaning service Company which have simple rules and we would like to show that(in checklist form) on website:

- What we do and that we're Cleaning Green

- Why us?

- How much(our pricing is simple)

Also we would like to communicate with clients by some nice/big pictures on website and the most important thing is our phone number and short/fast Freestimate.

Also there should be some space for description about our Company.

Generally all information on main page can be short: about us, about service(what we do), last reviews, tips (for example: Tip of the week) and other can be some introduction to subpage where will be more information.

There will be few subpages like: About us, About our service, Photos(Before and after), Reviews , Tips, FAQ, Contact, Looking for a Job? - most of them will be just text so you can project just one example.

```html
<!DOCTYPE html>
<html lang="en">
<head>
<meta charset="utf-8">
<title>Tidy Nest – House Cleaning</title>
<link rel="stylesheet" href="https://fonts.googleapis.com/css2?family=Oswald:wght@400;500&family=Arimo:wght@400;700&family=Schoolbell&family=Merienda:wght@400&display=swap">
<style>
:root{
  --green:#5db85a;
  --green-dark:#3f9c3d;
  --green-nav:rgba(94,184,90,.88);
  --green-footer:#7cc479;
  --green-bar:#52a84f;
  --text:#5a5a5a;
  --text-light:#8a8a8a;
  --rule:#dcdcdc;
  --paper:#f6f6f4;
  --white:#ffffff;
}
*{margin:0;padding:0;box-sizing:border-box}
html,body{width:736px;height:1200px;overflow:hidden}
body{background:var(--paper);font-family:"Arimo",Arial,sans-serif;color:var(--text);position:relative}
.abs{position:absolute}

/* header */
.brand{left:28px;top:30px;display:flex;align-items:center;gap:10px}
.brand-dot{width:22px;height:22px;border-radius:50%;background:var(--green)}
.brand-name{font-family:"Arimo",Arial,sans-serif;font-weight:700;font-size:24px;color:var(--green-dark)}
.brand-tag{left:60px;top:62px;font-size:11px;color:var(--green-dark)}
.header-contact{left:528px;top:30px;width:130px}
.header-contact .call{font-weight:700;font-size:19px;color:var(--green);white-space:nowrap}
.header-contact .line{height:2px;background:var(--green);margin:5px 0 8px}
.header-contact p{font-weight:700;font-size:11.5px;color:var(--green);line-height:24px;white-space:nowrap}

/* hero */
.hero-top{left:0;top:114px;width:736px;height:4px;background:var(--green)}
.hero-photo{left:0;top:118px;width:736px;height:212px;background:linear-gradient(100deg,#d9c9b0 0%,#efe7d8 30%,#c9b79b 55%,#8a7458 80%,#5d4a37 100%)}
.hero-band{left:0;top:169px;width:393px;height:131px;background:rgba(94,184,90,.72)}
.hero-title{left:97px;top:196px;font-family:"Oswald",sans-serif;font-weight:500;color:var(--white);font-size:35px;line-height:44px;letter-spacing:.5px}
.hero-title span{display:block;border-bottom:2px solid var(--white);width:max-content;line-height:40px;margin-bottom:4px}
.hero-title span+span{border:0}
.nav{left:0;top:328px;width:736px;height:45px;background:var(--green-nav);display:flex;align-items:center;padding-left:83px;gap:0}
.nav a{font-family:"Oswald",sans-serif;font-size:15px;color:var(--white);text-decoration:none;margin-right:39px;padding-bottom:3px}
.nav a.active{border-bottom:2px solid var(--white)}

/* feature cards */
.card{top:423px;width:166px}
.card-photo{height:104px;position:relative}
.card-label{position:absolute;left:0;bottom:0;width:100%;height:28px;background:rgba(94,184,90,.82);color:var(--white);font-family:"Oswald",sans-serif;font-size:14px;text-align:center;line-height:28px}
.card p,.card li{font-size:10px;line-height:14px;color:var(--text);margin-top:0}
.card .body{margin-top:16px;height:74px}
.card ul{list-style:none}
.card li{margin-bottom:10px}
.more{position:absolute;left:99px;top:195px;width:66px;height:24px;background:var(--green);color:var(--white);font-family:"Oswald",sans-serif;font-size:11px;text-align:center;line-height:24px}
.divider-v{width:1px;background:var(--rule)}

/* intro */
.intro{left:95px;top:700px;width:546px;text-align:center;font-size:10px;line-height:17px;color:var(--text-light)}
.intro .script{font-family:"Merienda",cursive;font-size:18px;color:var(--green)}
.star-rule{left:98px;top:768px}

/* why / pricing */
.why-title,.price-title{font-family:"Schoolbell",cursive;font-size:28px;color:#333}
.why-title{left:153px;top:815px}
.why-list{left:153px;top:857px;list-style:none}
.why-list li{font-size:9.5px;line-height:17.3px;color:var(--text)}
.price-title{left:417px;top:818px}
.price-row{font-size:9.5px;color:var(--text);white-space:nowrap}
.price-row b{font-family:"Merienda",cursive;font-weight:400;font-size:19px;color:var(--green);margin-right:4px}
.price-note{left:417px;top:935px;font-size:9.5px;color:var(--text)}
.price-small{left:417px;top:956px;font-size:7.5px;color:var(--text-light)}

/* footer */
.footer{left:0;top:1020px;width:736px;height:148px;background:var(--green-footer);border-top:2px solid var(--green)}
.footer-call{left:79px;top:1050px;font-family:"Schoolbell",cursive;font-size:24px;color:var(--white)}
.footer-contact{left:79px;top:1087px;font-weight:700;font-size:11.5px;color:var(--white);line-height:20px}
.footer-col{top:1048px;color:var(--white)}
.footer-col h4{font-size:11.5px;font-weight:700;margin-bottom:12px}
.footer-col p,.footer-col li{font-size:7.5px;line-height:11px}
.footer-col ul{list-style:none}
.bottom-bar{left:0;top:1168px;width:736px;height:32px;background:var(--green-bar);color:var(--white);font-size:8px;text-align:center;line-height:32px}
</style>
</head>
<body>

<header>
  <div class="brand abs"><span class="brand-dot"></span><span class="brand-name">Tidy Nest</span></div>
  <div class="brand-tag abs">house cleaning</div>
  <div class="header-contact abs">
    <div class="call">Call Us Today!</div>
    <div class="line"></div>
    <p>555-014-2730</p>
    <p>www.HarbourTidyNest.ca</p>
  </div>
</header>

<section class="hero">
  <div class="hero-top abs"></div>
  <div class="hero-photo abs" role="img" aria-label="Smiling family with their dog relaxing in a bright, clean living room"></div>
  <div class="hero-band abs"></div>
  <h1 class="hero-title abs"><span>WE'RE TIDY NEST</span><span>WE'RE CLEANING GREEN</span></h1>
  <nav class="nav abs">
    <a class="active" href="#">HOME</a><a href="#">ABOUT US</a><a href="#">SERVICES</a><a href="#">PHOTOS</a><a href="#">REVIEWS</a><a href="#">TIPS</a><a href="#">FAQ</a><a href="#">CONTACT</a>
  </nav>
</section>

<section class="features">
  <article class="card abs" style="left:81px">
    <div class="card-photo" role="img" aria-label="Couple outdoors on a sunny winter day" style="background:linear-gradient(180deg,#6fa6d8 0%,#a9cdeb 55%,#e9eef2 100%)"><div class="card-label">ABOUT US</div></div>
    <div class="body"><p>It's about caring, not just cleaning. Having personally experienced the struggles of finding quality maid service for our home, we want to make it simpler for families in the Lakeside area.</p></div>
    <a class="more">MORE</a>
  </article>
  <div class="divider-v abs" style="left:265px;top:423px;height:218px"></div>
  <article class="card abs" style="left:285px">
    <div class="card-photo" role="img" aria-label="Friendly receptionist taking a booking call by phone" style="background:linear-gradient(90deg,#e9ecef 0%,#d4d9de 50%,#6b5a4e 100%)"><div class="card-label">ABOUT SERVICE</div></div>
    <div class="body"><ul><li>• Thoroughly clean your bathrooms, kitchen, bedrooms and living areas</li><li>• Mop or vacuum your floors</li><li>• Dust surfaces</li></ul></div>
    <a class="more">MORE</a>
  </article>
  <div class="divider-v abs" style="left:470px;top:423px;height:218px"></div>
  <article class="card abs" style="left:489px">
    <div class="card-photo" role="img" aria-label="Group of happy senior clients standing on a green lawn" style="background:linear-gradient(180deg,#9ec58a 0%,#c8d9b5 45%,#7fae66 100%)"><div class="card-label">LAST REVIEWS</div></div>
    <div class="body"><p>It's about caring, not just cleaning. Having personally experienced the struggles of finding quality maid service for our home, we want to make it simpler for families in the Lakeside area.</p></div>
    <a class="more">MORE</a>
  </article>
</section>

<section>
  <p class="intro abs">Have you ever wondered what it would be like if your life was simpler? We're here to help by taking over the chore of house cleaning. You'll have more time to spend on the things that matter most to you.<br>With <span class="script">Tidy Nest</span> you get reliable, trustworthy and affordable maid service. We pay attention to your needs. We get the job done!</p>
  <svg class="star-rule abs" width="540" height="16" viewBox="0 0 540 16">
    <line x1="0" y1="8" x2="258" y2="8" stroke="#dcdcdc"/>
    <line x1="282" y1="8" x2="540" y2="8" stroke="#dcdcdc"/>
    <polygon points="270,2 271.8,6.5 276.5,6.6 272.8,9.5 274.1,14 270,11.3 265.9,14 267.2,9.5 263.5,6.6 268.2,6.5" fill="#5db85a"/>
  </svg>
</section>

<section>
  <h2 class="why-title abs">Why choose us?</h2>
  <ul class="why-list abs">
    <li>• Owners Present at Every Cleaning</li>
    <li>• Locally Owned &amp; Operated</li>
    <li>• Reliable &amp; Affordable</li>
    <li>• All Supplies Provided</li>
    <li>• Green Cleaning</li>
    <li>• Pet Friendly</li>
    <li>• No Contracts</li>
  </ul>
  <div class="divider-v abs" style="left:380px;top:826px;height:148px"></div>
  <h2 class="price-title abs">Pricing is.. simple.</h2>
  <div class="price-row abs" style="left:417px;top:852px"><b>$79</b>for homes less than 1000 sq ft</div>
  <div class="price-row abs" style="left:440px;top:878px"><b>$89</b>for homes 1000-1800 sq ft</div>
  <div class="price-row abs" style="left:417px;top:905px"><b>$99</b>for homes 1800-2600 sq ft</div>
  <p class="price-note abs">*If your home is larger than 2600 sq ft please call for a quote.</p>
  <p class="price-small abs">*rates are for regular service*</p>
</section>

<footer>
  <div class="footer abs"></div>
  <div class="footer-call abs">Call Us Today!</div>
  <div class="footer-contact abs">555-014-2730<br>www.HarbourTidyNest.ca</div>
  <div class="footer-col abs" style="left:309px;width:150px">
    <h4>services</h4>
    <ul>
      <li>• Thoroughly clean your bathrooms, kitchen, bedrooms and living areas</li>
      <li>• Mop or vacuum your floors</li>
      <li>• Dust surfaces</li>
      <li>• Collect garbage</li>
      <li>• Make beds</li>
    </ul>
  </div>
  <div class="footer-col abs" style="left:500px;width:152px">
    <h4>FAQ</h4>
    <p>Question: How much do I need to pay for a full service for my new house?</p>
    <p style="margin-top:10px">Answer: Hello, it depends on the size of your house. Thank you for your question and please add more details.</p>
    <p style="margin-top:3px;font-weight:700">... ...</p>
  </div>
  <div class="bottom-bar abs">© 2013 Tidy Nest. All rights reserved.</div>
</footer>

</body>
</html>
```